New Business Card Design

We would like to refresh our business cards and make them look better. We are an IT company specialising in Cloud Services, IT Managed Services, software and hardware. I have attached a PSD of our current design. Also attached our logo.
Updates

I have uploaded all new logos in EPS format.

Can you please edit all designs to include a job title for Marcus Hale, eg. General Manager

Industry/Entity Type

Software

Colors
ffffff

Requirements
Must have
• Please use white background.
Should not have
• Black background

```html
<!DOCTYPE html>
<html lang="en">
<head>
<meta charset="utf-8">
<title>Northvale Technology – Business Card</title>
<link rel="stylesheet" href="https://fonts.googleapis.com/css2?family=Source+Sans+3:wght@300;400;600&display=swap">
<style>
  :root {
    --canvas: #ffffff;
    --brand-red: #ed1c24;
    --accent-red: #e8312a;
    --name-orange: #f5a623;
    --name-red: #c0392b;
    --text-dark: #1f1f1f;
    --text-body: #4a4a4a;
    --text-grey: #7d8288;
    --rule-grey: #9a9a9a;
    --rule-dark: #2b2b2b;
    --card-border: #e4e8dc;
    --ornament-light: #f4785f;
  }
  * { margin: 0; padding: 0; box-sizing: border-box; }
  html, body { width: 1200px; height: 362px; overflow: hidden; background: var(--canvas); }
  body { position: relative; font-family: "Source Sans 3", "Segoe UI", Arial, sans-serif; }

  .card { position: absolute; overflow: hidden; }
  .card--front { left: 43px; top: 28px; width: 532px; height: 296px; background: var(--brand-red); }
  .card--back { left: 604px; top: 27px; width: 532px; height: 296px; background: var(--canvas); border: 1px solid var(--card-border); }

  .front-ornament {
    position: absolute; left: 0; top: 140px; width: 240px; height: 156px;
    background: radial-gradient(ellipse at 15% 85%, var(--ornament-light) 0%, rgba(244,120,95,0.35) 45%, rgba(237,28,36,0) 75%);
  }
  .front-brand { position: absolute; left: 36px; top: 62px; display: flex; align-items: center; gap: 18px; }
  .front-brand__mark { width: 58px; height: 58px; border-radius: 50%; background: #fff; }
  .front-brand__name {
    color: #fff; font-weight: 300; font-size: 34px; line-height: 0.95; letter-spacing: 6px;
  }
  .front-brand__name span { display: block; font-size: 19px; letter-spacing: 4.5px; margin-top: 6px; }

  .divider { position: absolute; left: 231px; width: 2px; }
  .divider--grey { top: 19px; height: 18px; background: var(--rule-grey); }
  .divider--dark { top: 40px; height: 48px; background: var(--rule-dark); }
  .divider--red { top: 92px; height: 190px; background: var(--accent-red); }

  .person { position: absolute; left: 245px; top: 43px; }
  .person__name { font-size: 25px; line-height: 1; letter-spacing: 0.2px; }
  .person__first { color: var(--name-orange); font-weight: 400; }
  .person__last { color: var(--name-red); font-weight: 600; }
  .person__rule { width: 166px; height: 1px; background: var(--name-orange); margin-top: 3px; }
  .person__title { font-size: 11px; color: var(--text-body); margin-top: 2px; }

  .services { position: absolute; right: 316px; top: 92px; list-style: none; text-align: right; }
  .services li { font-size: 12.5px; color: var(--text-body); line-height: 25px; }
  .services li::after {
    content: ""; display: inline-block; width: 5px; height: 5px; border-radius: 50%;
    background: var(--accent-red); margin-left: 9px; vertical-align: middle;
  }

  .contact { position: absolute; left: 246px; list-style: none; }
  .contact--phones { top: 123px; }
  .contact--phones li { display: flex; align-items: center; font-size: 19px; color: var(--text-grey); line-height: 25px; }
  .contact__badge {
    display: inline-flex; width: 17px; height: 17px; border-radius: 50%; margin-left: 13px;
    background: var(--accent-red); color: #fff; font-size: 11px; font-weight: 600;
    align-items: center; justify-content: center;
  }
  .contact__email { position: absolute; left: 246px; top: 182px; font-size: 18px; color: var(--text-dark); }
  .contact__web { position: absolute; left: 246px; top: 225px; font-size: 18px; color: var(--text-grey); }

  .back-brand { position: absolute; left: 70px; top: 243px; display: flex; align-items: center; gap: 8px; }
  .back-brand__mark { width: 22px; height: 22px; border-radius: 50%; background: var(--accent-red); }
  .back-brand__name { font-size: 15px; font-weight: 400; color: var(--text-dark); letter-spacing: 1.8px; line-height: 1; }
  .back-brand__name span { display: block; font-size: 8px; letter-spacing: 2px; margin-top: 2px; }
</style>
</head>
<body>
  <section class="card card--front">
    <div class="front-ornament" role="img" aria-label="Soft floral swirl ornament in light red tones"></div>
    <div class="front-brand">
      <div class="front-brand__mark"></div>
      <div class="front-brand__name">northvale<span>TECHNOLOGY</span></div>
    </div>
  </section>

  <section class="card card--back">
    <div class="divider divider--grey"></div>
    <div class="divider divider--dark"></div>
    <div class="divider divider--red"></div>

    <div class="person">
      <div class="person__name"><span class="person__first">Marcus</span><span class="person__last">Hale</span></div>
      <div class="person__rule"></div>
      <div class="person__title">General Manager</div>
    </div>

    <ul class="services">
      <li>Cloud Services</li>
      <li>Hardware</li>
      <li>Software</li>
      <li>It Managed Services</li>
    </ul>

    <ul class="contact contact--phones">
      <li>07 5550 1414 <span class="contact__badge">M</span></li>
      <li>0400 555 218 <span class="contact__badge">P</span></li>
    </ul>
    <div class="contact__email">mhale@northvaleit.com.au</div>
    <div class="contact__web">www.northvaleit.com.au</div>

    <div class="back-brand">
      <div class="back-brand__mark"></div>
      <div class="back-brand__name">northvale<span>TECHNOLOGY</span></div>
    </div>
  </section>
</body>
</html>
```